Business card for Eyelash extension salon in Beverly Hills,California USA

We need new business card for our salon in Beverly Hills. The salon name is 'Lashvora' . We would like to have...Business name: Lashvora Name of person: will provide later Address 6812 N.Calder Ridge Ave Beverly Hills , CA 90210 Phone: will provide later (Text only) Web: www.lashvorastudio-demo.com Instagram icon, Facebook icon follow us for seasonal campaign and news @lashvorastudiodemo Design should look elegant, high-end, clean, simple, cohesive with my brand. Please refer my brand board. Business name color will be metallic bronzy color. Im thinking grey background or white background. Thanks

Target Market(s)

25-35. Gender neutral. People who are in Entertainment business industry.
This is High-end Eyelash extension salon in Beverly Hills

Industry/Entity Type

Beauty Salon

Contact Information for Business Card

Business name: Lashvora
Name of person: will provide later
Address 6812 N.Calder Ridge Ave Beverly Hills , CA 90210
Phone: will provide later (Text only)
Web: www.lashvorastudio-demo.com
Instagram icon, Facebook icon
follow us for seasonal campaign and news @lashvorastudiodemo

Requirements
Must have
• Beautiful, elegant, clean and simple look but very attractive and modern
Should not have
• We don't like too clutter, too busy designs.

```html
<!DOCTYPE html>
<html lang="en">
<head>
<meta charset="utf-8">
<title>Lashvora Beverly Hills – Business Card</title>
<link rel="stylesheet" href="https://fonts.googleapis.com/css2?family=Saira+Semi+Condensed:wght@400;500&display=swap">
<style>
  :root {
    --stage-grey: #666666;
    --card-paper: #f6f5f5;
    --bronze-deep: #86634a;
    --bronze-warm: #b98a55;
    --lotus-haze: #ffffff;
  }
  * { margin: 0; padding: 0; box-sizing: border-box; }
  html, body {
    width: 1200px;
    height: 1000px;
    overflow: hidden;
    background: var(--stage-grey);
    font-family: "Saira Semi Condensed", "Arial Narrow", sans-serif;
  }
  .stage { position: relative; width: 1200px; height: 1000px; }

  .card {
    position: absolute;
    width: 712px;
    height: 452px;
    background: var(--card-paper);
    border-radius: 58px;
    overflow: hidden;
  }
  .card--front { left: 246px; top: 18px; }
  .card--back  { left: 244px; top: 532px; }

  .lotus-motif {
    position: absolute;
    width: 226px;
    height: 180px;
    border-radius: 50% 50% 40% 40%;
    background: radial-gradient(ellipse at center, rgba(255,255,255,0.9) 0%, rgba(255,255,255,0.35) 55%, rgba(255,255,255,0) 75%);
  }
  .card--front .lotus-motif--top    { left: 24px;  top: 0; }
  .card--front .lotus-motif--corner { left: 459px; top: 270px; }
  .card--back  .lotus-motif--top    { left: 461px; top: 0; }
  .card--back  .lotus-motif--bottom { left: 28px;  top: 278px; }

  .brand {
    position: absolute;
    left: 0;
    width: 100%;
    text-align: center;
    color: var(--bronze-deep);
  }
  .brand__name {
    top: 110px;
    font-size: 118px;
    font-weight: 400;
    line-height: 1;
    letter-spacing: 2px;
  }
  .brand__place {
    top: 256px;
    left: 342px;
    width: auto;
    font-size: 14px;
    letter-spacing: 3.4px;
    text-align: left;
  }

  .contact-list {
    position: absolute;
    left: 62px;
    top: 142px;
    list-style: none;
    color: var(--bronze-warm);
    font-size: 19px;
    font-weight: 500;
  }
  .contact-list__item {
    display: flex;
    align-items: center;
    height: 24px;
    margin-bottom: 12px;
  }
  .contact-list__icon {
    width: 24px;
    height: 24px;
    margin-right: 13px;
    display: flex;
    align-items: center;
    justify-content: center;
    fill: var(--bronze-warm);
    font-size: 22px;
    font-weight: 500;
  }
  .contact-list__social-mark {
    width: 20px;
    height: 20px;
    margin: 0 15px 0 2px;
    background: var(--bronze-warm);
    border-radius: 3px;
  }
</style>
</head>
<body>
<main class="stage">

  <section class="card card--front" aria-label="Card front">
    <div class="lotus-motif lotus-motif--top" role="img" aria-label="Faint white line-art lotus flower decoration"></div>
    <div class="lotus-motif lotus-motif--corner" role="img" aria-label="Faint white line-art lotus flower decoration"></div>
    <h1 class="brand brand__name">Lashvora</h1>
    <p class="brand brand__place">BEVERLY HILLS</p>
  </section>

  <section class="card card--back" aria-label="Card back">
    <div class="lotus-motif lotus-motif--top" role="img" aria-label="Faint white line-art lotus flower decoration"></div>
    <div class="lotus-motif lotus-motif--bottom" role="img" aria-label="Faint white line-art lotus flower decoration"></div>

    <ul class="contact-list">
      <li class="contact-list__item">
        <span class="contact-list__icon">
          <svg viewBox="0 0 24 24" width="20" height="20" aria-hidden="true">
            <path d="M6.6 10.8c1.4 2.8 3.8 5.1 6.6 6.6l2.2-2.2c.3-.3.7-.4 1-.2 1.1.4 2.3.6 3.6.6.6 0 1 .4 1 1V20c0 .6-.4 1-1 1C10.6 21 3 13.4 3 4c0-.6.4-1 1-1h3.5c.6 0 1 .4 1 1 0 1.3.2 2.5.6 3.6.1.3 0 .7-.2 1l-2.3 2.2z"/>
          </svg>
        </span>
      </li>
      <li class="contact-list__item">
        <span class="contact-list__icon">@</span>
      </li>
      <li class="contact-list__item">
        <span class="contact-list__icon">
          <svg viewBox="0 0 24 24" width="22" height="22" aria-hidden="true">
            <path d="M12 3 2 12h3v8h5v-5h4v5h5v-8h3z"/>
          </svg>
        </span>
        <span>6812 N.Calder Ridge Ave Beverly Hills , CA 90210</span>
      </li>
      <li class="contact-list__item">
        <span class="contact-list__icon">
          <svg viewBox="0 0 24 24" width="22" height="22" aria-hidden="true" fill="none" stroke="#b98a55" stroke-width="1.8">
            <circle cx="12" cy="12" r="10"/>
            <ellipse cx="12" cy="12" rx="4.5" ry="10"/>
            <line x1="2" y1="12" x2="22" y2="12"/>
            <line x1="12" y1="2" x2="12" y2="22"/>
            <path d="M4 7h16M4 17h16"/>
          </svg>
        </span>
        <span>www.lashvorastudio-demo.com</span>
      </li>
      <li class="contact-list__item">
        <span class="contact-list__social-mark" aria-hidden="true"></span>
        <span>@lashvorastudiodemo</span>
      </li>
    </ul>
  </section>

</main>
</body>
</html>
```